Men's and Boys sports themed barbershop. I was wanting to see what a black card would look like. I think white is too plain, but I am just needing some ideas for a design or background.

Contact Information for Business Card

Ace Trims
4826 E. Harbor Pine Rd
Crystal River, Fl 34512
(352) 555-0142
ace_trims@quellmail.com
Denise Marlow (on one side) Gregory Marlow (on opposite side)
Owner
(352) 555-0187 (Denise) (352) 555-0163

```html
<!DOCTYPE html>
<html lang="en">
<head>
<meta charset="utf-8">
<title>Ace Trims – Business Cards</title>
<link href="https://fonts.googleapis.com/css2?family=Crimson+Text:wght@400;600&display=swap" rel="stylesheet">
<style>
  :root {
    --backdrop: #7b7b7b;
    --card-center: #3b3b3b;
    --card-edge: #0c0c0c;
    --brand-red: #c8202b;
    --text-white: #f4f4f4;
    --icon-grey: #9a9a9a;
  }
  * { margin: 0; padding: 0; box-sizing: border-box; }
  html, body {
    width: 1200px; height: 1000px; overflow: hidden;
    background: var(--backdrop);
  }
  .canvas { position: relative; width: 1200px; height: 1000px; }
  .card {
    position: absolute;
    background: radial-gradient(ellipse at 45% 48%, var(--card-center) 0%, #1c1c1c 45%, var(--card-edge) 100%);
    color: var(--text-white);
    font-family: "Crimson Text", Georgia, serif;
    overflow: hidden;
  }
  .card--front { left: 49px; top: 47px; width: 761px; height: 436px; }
  .card--back { left: 372px; top: 515px; width: 776px; height: 442px; }

  .brand-name {
    position: absolute;
    width: 560px;
    text-align: center;
    font-family: "Crimson Text", Georgia, serif;
    font-weight: 600;
    font-size: 92px;
    line-height: 1;
    color: var(--brand-red);
    white-space: nowrap;
  }
  .card--front .brand-name { left: 30px; top: 80px; }
  .card--back .brand-name { left: 130px; top: 62px; }

  .contact-list {
    position: absolute; left: 34px; top: 326px;
    list-style: none; font-size: 20px; line-height: 25px;
  }
  .contact-list li { display: flex; align-items: center; gap: 8px; white-space: nowrap; }
  .icon { width: 26px; height: 20px; flex: none; }
  .icon path, .icon rect, .icon circle { fill: none; stroke: var(--icon-grey); stroke-width: 1.4; }

  .owner {
    position: absolute; top: 305px;
    white-space: nowrap;
  }
  .owner--left { left: 33px; text-align: left; }
  .owner--right { right: 23px; text-align: right; }
  .owner-name { font-size: 50px; line-height: 52px; }
  .owner-role { font-size: 27px; line-height: 28px; }
  .owner-phone {
    margin-top: 6px; font-size: 21px;
    display: flex; align-items: center; gap: 6px;
  }
  .owner--right .owner-phone { justify-content: flex-end; }
</style>
</head>
<body>
<div class="canvas">

  <section class="card card--front" aria-label="Card front">
    <div class="brand-name">Ace Trims</div>
    <ul class="contact-list">
      <li>
        <svg class="icon" viewBox="0 0 26 20" aria-hidden="true"><path d="M2 10 L13 2 L24 10"/><rect x="5" y="9" width="16" height="10"/><rect x="11" y="13" width="4" height="6"/></svg>
        4826 E. Harbor Pine Rd Crystal River, Fl 34512
      </li>
      <li>
        <svg class="icon" viewBox="0 0 26 20" aria-hidden="true"><path d="M2 8 Q13 0 24 8 L21 10 L18 8 L8 8 L5 10 Z"/><rect x="5" y="10" width="16" height="9"/><circle cx="13" cy="14.5" r="2.5"/></svg>
        (352) 555-0142
      </li>
      <li>
        <svg class="icon" viewBox="0 0 26 20" aria-hidden="true"><rect x="2" y="3" width="22" height="15"/><path d="M2 3 L13 12 L24 3"/></svg>
        ace_trims@quellmail.com
      </li>
    </ul>
  </section>

  <section class="card card--back" aria-label="Card back">
    <div class="brand-name">Ace Trims</div>

    <div class="owner owner--left">
      <div class="owner-name">Gregory Marlow</div>
      <div class="owner-role">(Owner)</div>
      <div class="owner-phone">
        <svg class="icon" viewBox="0 0 26 20" aria-hidden="true"><path d="M2 8 Q13 0 24 8 L21 10 L18 8 L8 8 L5 10 Z"/><rect x="5" y="10" width="16" height="9"/><circle cx="13" cy="14.5" r="2.5"/></svg>
        (352) 555-0187
      </div>
    </div>

    <div class="owner owner--right">
      <div class="owner-name">Denise Marlow</div>
      <div class="owner-role">(Owner)</div>
      <div class="owner-phone">
        <svg class="icon" viewBox="0 0 26 20" aria-hidden="true"><path d="M2 8 Q13 0 24 8 L21 10 L18 8 L8 8 L5 10 Z"/><rect x="5" y="10" width="16" height="9"/><circle cx="13" cy="14.5" r="2.5"/></svg>
        (352) 555-0163
      </div>
    </div>
  </section>

</div>
</body>
</html>
```